Website design to promote trampoline business

We require a website design for our business. The business is primarily provising access for people between 5YO and 40YO to jump on trampolines for fun and fitness.

We have a logo and color schemes already and the website should incorporate these colors and designs.

We would like to incorporate the following pages:-

Book Now!
Home
About Us
Locations & Hours
Jumping
Groups & Events
Gallery
Safety
Latest News
Careers

Industry/Entity Type

Business

Requirements
Must have
• Incorporate our logo and colors (files attached).

```html
<!DOCTYPE html>
<html lang="en">
<head>
<meta charset="utf-8">
<title>HopZone Trampolines</title>
<link href="https://fonts.googleapis.com/css2?family=Roboto:wght@300;400;500;700&display=swap" rel="stylesheet">
<style>
:root{
  --orange:#f7941d;
  --blue:#29abe2;
  --sky:#4fb9e6;
  --sky-light:#a9dcf2;
  --grass:#6b9a2e;
  --grass-dark:#5a8a25;
  --ink:#333;
  --text:#666;
  --line:#ddd;
  --footer:#f4f4f4;
  --white:#fff;
}
*{margin:0;padding:0;box-sizing:border-box}
html,body{width:790px;height:1200px;overflow:hidden;background:var(--white)}
body{position:relative;font-family:'Roboto',sans-serif;color:var(--ink)}
.abs{position:absolute}
.logo{font-weight:700;color:var(--orange);font-size:24px;letter-spacing:1px;line-height:1}
.logo-sub{font-size:8px;color:var(--text);letter-spacing:1px;font-weight:400}
.search{left:431px;top:30px;width:180px;height:22px;border:1px solid var(--line);border-radius:2px;font-size:9px;color:#aaa;padding:5px 9px}
.search-btn{left:588px;top:30px;width:23px;height:22px;border-left:1px solid var(--line)}
.social{top:30px;width:20px;height:20px;border-radius:50%}
.nav{left:0;top:75px;width:790px;height:33px;background:var(--orange)}
.nav a{position:absolute;top:0;height:33px;line-height:33px;color:var(--white);font-size:10px;text-decoration:none}
.nav a.active{background:var(--blue);padding:0 8px}
.hero{left:0;top:108px;width:790px;height:362px;overflow:hidden}
.hero-art{left:197px;top:108px;width:358px;height:362px;background:radial-gradient(ellipse at 50% 55%,rgba(255,255,255,.22) 0%,rgba(255,255,255,.08) 45%,rgba(255,255,255,0) 70%)}
.hero-kicker{left:92px;top:352px;color:var(--white);font-weight:700;font-size:15px;letter-spacing:-.5px}
.hero-title{left:91px;top:366px;color:var(--white);font-weight:500;font-size:30px;letter-spacing:-1px}
.hero-tag{left:92px;top:402px;color:var(--white);font-weight:300;font-size:13px;line-height:16px}
.cta{top:258px;height:24px;line-height:20px;color:var(--white);font-size:8px;font-weight:700;border:2px solid var(--white);border-radius:3px}
.cta-party{left:573px;width:84px;background:#8cb83a;text-align:center;margin-top:4px}
.cta-now{left:655px;width:40px;background:var(--orange);text-align:center;height:32px;line-height:12px;padding-top:3px;font-size:9px}
.post{left:629px;top:286px;width:5px;height:38px;background:#eee}
h2{font-weight:500;font-size:17px;color:var(--ink)}
.vline{top:505px;width:1px;height:312px;background:var(--line)}
.hline{left:90px;width:609px;height:1px;background:var(--line)}
.date{left:90px;color:var(--blue);line-height:1}
.date b{display:block;font-size:18px;font-weight:500}
.date span{font-size:8px}
.ev-title{left:120px;font-size:8.5px;text-transform:uppercase;color:var(--ink)}
.body{font-size:8.5px;color:var(--text);line-height:10.5px}
.more{font-size:8.5px;color:var(--ink)}
.dots{left:90px;width:168px;border-top:1px dotted #bbb}
.caps{font-size:8px;text-transform:uppercase;color:var(--ink);line-height:11px}
.photo{border-radius:1px}
.svc-icon{left:529px;width:33px;height:33px;border:1px solid var(--line);background:#fafafa}
.svc-title{left:566px;font-size:8.5px;font-weight:700;color:var(--blue);text-transform:uppercase}
.quote{left:96px;color:var(--blue);font-size:20px;font-weight:700;line-height:1}
.partner-mark{width:20px;height:20px;border-radius:50%;background:#8a8a8a}
.partner-name{font-size:8px;color:var(--text);text-transform:uppercase;line-height:11px}
.partner-name span{text-transform:none;font-size:9px;color:#777}
.footer{left:0;top:1123px;width:790px;height:77px;background:var(--footer);border-top:1px solid #e6e6e6}
.footer-nav a{position:absolute;top:1142px;font-size:8px;color:var(--text);text-decoration:none}
.copy{left:92px;top:1174px;font-size:8px;color:var(--text)}
</style>
</head>
<body>

<header>
  <div class="abs" style="left:90px;top:20px">
    <div class="logo">HOPZONE</div>
    <div class="logo-sub">Trampolines</div>
  </div>
  <div class="abs search">Search</div>
  <div class="abs search-btn">
    <svg width="23" height="22" viewBox="0 0 23 22"><circle cx="10.5" cy="10" r="4" fill="none" stroke="#aaa" stroke-width="1.3"/><line x1="13.5" y1="13" x2="17" y2="16.5" stroke="#aaa" stroke-width="1.5"/></svg>
  </div>
  <div class="abs" style="left:622px;top:20px;width:1px;height:42px;background:var(--line)"></div>
  <div class="abs social" style="left:629px;background:#3b5998"></div>
  <div class="abs social" style="left:654px;background:#29a9e1"></div>
  <div class="abs social" style="left:678px;background:#d12a27"></div>
</header>

<nav class="abs nav">
  <a class="active" href="#" style="left:90px">Home</a>
  <a href="#" style="left:141px">Careers</a>
  <a href="#" style="left:192px">About Us</a>
  <a href="#" style="left:249px">Locations &amp; Hours</a>
  <a href="#" style="left:346px">Jumping</a>
  <a href="#" style="left:402px">Groups &amp; Events</a>
  <a href="#" style="left:490px">Gallery</a>
  <a href="#" style="left:538px">Safety</a>
  <a href="#" style="left:584px">Latest News</a>
</nav>

<section>
  <svg class="abs hero" width="790" height="362" viewBox="0 0 790 362">
    <defs>
      <linearGradient id="skyGrad" x1="0" y1="0" x2="0" y2="1">
        <stop offset="0" stop-color="#4fb9e6"/>
        <stop offset="0.75" stop-color="#a9dcf2"/>
      </linearGradient>
      <linearGradient id="grassGrad" x1="0" y1="0" x2="0" y2="1">
        <stop offset="0" stop-color="#76a534"/>
        <stop offset="1" stop-color="#5e8d27"/>
      </linearGradient>
    </defs>
    <rect width="790" height="362" fill="url(#skyGrad)"/>
    <path d="M0 188 C120 200 220 230 330 226 C450 222 560 240 650 262 C710 276 760 284 790 286 L790 362 L0 362 Z" fill="url(#grassGrad)"/>
  </svg>
  <div class="abs hero-art" role="img" aria-label="Cartoon of two happy children jumping on a blue trampoline in a green meadow under a blue sky"></div>
  <div class="abs hero-kicker">HOPZONE</div>
  <div class="abs hero-title">Trampoline</div>
  <div class="abs hero-tag">A revolutionary design<br>that’s strong and safe.</div>
  <div class="abs post"></div>
  <div class="abs cta cta-party">Book Your Party</div>
  <div class="abs cta cta-now">Now!<br>→</div>
</section>

<section>
  <h2 class="abs" style="left:90px;top:499px">Events calendar</h2>
  <div class="abs vline" style="left:277px"></div>
  <div class="abs vline" style="left:512px"></div>

  <div class="abs date" style="top:542px"><b>20</b><span>MAR</span></div>
  <div class="abs ev-title" style="top:544px">Lorem ipsum dolor sit amet</div>
  <div class="abs body" style="left:120px;top:558px">Lorem ipsum dolor sit amet,<br>constuer adipiscing elit,</div>
  <div class="abs more" style="left:120px;top:592px">more info</div>
  <div class="abs dots" style="top:615px"></div>

  <div class="abs date" style="top:629px"><b>20</b><span>MAR</span></div>
  <div class="abs ev-title" style="top:631px">Lorem ipsum dolor sit amet</div>
  <div class="abs body" style="left:120px;top:645px">Lorem ipsum dolor sit amet,<br>constuer adipiscing elit,</div>
  <div class="abs more" style="left:120px;top:680px">more info</div>
  <div class="abs dots" style="top:706px"></div>

  <div class="abs date" style="top:721px"><b>20</b><span>MAR</span></div>
  <div class="abs ev-title" style="top:723px">Lorem ipsum dolor sit amet</div>
  <div class="abs body" style="left:120px;top:737px">Lorem ipsum dolor sit amet,<br>constuer adipiscing elit,</div>
  <div class="abs more" style="left:120px;top:772px">more info</div>

  <h2 class="abs" style="left:291px;top:499px">Welcome to our site!</h2>
  <div class="abs caps" style="left:291px;top:544px;width:210px">Lorem ipsum dolor sit amet, consectetuer adiping elit, nonummy nibh euismod</div>
  <div class="abs photo" role="img" aria-label="Photo of two boys leaping on a garden trampoline under a cloudy sky" style="left:291px;top:573px;width:207px;height:137px;background:linear-gradient(180deg,#e9eef2 0%,#cfd9df 55%,#5f7d45 70%,#3d5a2e 100%)"></div>
  <div class="abs body" style="left:291px;top:723px;width:210px">Velit esse molestie consequat, vel illum dolore eu feugiat nulla facilisis at vero eros et accumsan et iusto odio dignissim qui blandit praesent luptatum zzril delenit augue duis ....</div>
  <div class="abs more" style="left:291px;top:772px">more info</div>

  <h2 class="abs" style="left:530px;top:499px">Latest services</h2>
  <div class="abs caps" style="left:530px;top:544px;width:172px">Lorem ipsum dolor sit amet, ctetuer adiping elit, sed diam</div>
  <div class="abs body" style="left:530px;top:573px;width:165px">Velit esse molestie consequat, vel illum dolore eu feugiat nla facilisis vero eros et accumsan eo odio dignim qui blandit praesent luum zzril delenit augue duis ....</div>

  <div class="abs svc-icon" style="top:640px">
    <svg width="31" height="31" viewBox="0 0 31 31"><ellipse cx="15.5" cy="19" rx="10" ry="2.5" fill="none" stroke="#333" stroke-width="1.6"/><line x1="8" y1="20.5" x2="7" y2="26" stroke="#333" stroke-width="1.6"/><line x1="23" y1="20.5" x2="24" y2="26" stroke="#333" stroke-width="1.6"/><circle cx="15.5" cy="9" r="2.5" fill="#333"/></svg>
  </div>
  <div class="abs svc-title" style="top:640px">Lorem ipsum dolor sit</div>
  <div class="abs body" style="left:567px;top:652px">Lorem ipsum dolor sit amet,<br>constuer adipiscing elit,</div>

  <div class="abs svc-icon" style="top:683px">
    <svg width="31" height="31" viewBox="0 0 31 31"><ellipse cx="15.5" cy="21" rx="10" ry="2.5" fill="none" stroke="#333" stroke-width="1.6"/><line x1="8" y1="22.5" x2="7" y2="27" stroke="#333" stroke-width="1.6"/><line x1="23" y1="22.5" x2="24" y2="27" stroke="#333" stroke-width="1.6"/><path d="M15.5 5 L15.5 13" stroke="#333" stroke-width="1.6"/><path d="M12 8 L15.5 6 L19 8" fill="none" stroke="#333" stroke-width="1.4"/></svg>
  </div>
  <div class="abs svc-title" style="top:683px">Lorem ipsum dolor sit</div>
  <div class="abs body" style="left:566px;top:695px">Lorem ipsum dolor sit amet,<br>constuer adipiscing elit,</div>

  <div class="abs svc-icon" style="top:727px">
    <svg width="31" height="31" viewBox="0 0 31 31"><line x1="6" y1="22" x2="25" y2="22" stroke="#333" stroke-width="1.8"/><line x1="9" y1="22" x2="9" y2="27" stroke="#333" stroke-width="1.6"/><line x1="22" y1="22" x2="22" y2="27" stroke="#333" stroke-width="1.6"/><path d="M11 15 L15.5 6 L20 15" fill="none" stroke="#333" stroke-width="1.6"/></svg>
  </div>
  <div class="abs svc-title" style="top:727px">Lorem ipsum dolor sit</div>
  <div class="abs body" style="left:567px;top:740px">Lorem ipsum dolor sit amet,<br>constuer adipiscing elit,</div>
  <div class="abs more" style="left:568px;top:772px">more info</div>
</section>

<div class="abs hline" style="top:829px"></div>

<section>
  <h2 class="abs" style="left:92px;top:858px">Testimonials</h2>
  <div class="abs quote" style="top:892px">“</div>
  <div class="abs body" style="left:116px;top:892px;width:160px">Velit esse molestie consequat, vel illum dolore eu feugiat nulla facilisis..</div>
  <div class="abs" style="left:116px;top:919px;font-size:7px">JOHNY D.</div>
  <div class="abs quote" style="top:941px">“</div>
  <div class="abs body" style="left:116px;top:941px;width:160px">Velit esse molestie consequat, vel illum dolore eu feugiat nulla facilisis..</div>
  <div class="abs" style="left:116px;top:968px;font-size:7px">EMMA S.</div>

  <h2 class="abs" style="left:312px;top:858px">Photostream</h2>
  <div class="abs" style="left:312px;top:880px;width:385px;font-size:8px;line-height:11px;color:var(--ink)">Lorem ipsum dolor sit amet, consectetuer adipiscing elit, sed diam nonummy nibh euismod tincidunt ut laoreet dolore magna aliquam erat volutpat. Ut wisi enim ad minim veniam, quis nfacilisis.</div>
  <div class="abs photo" role="img" aria-label="Photo of a girl jumping on a trampoline in front of a house" style="left:311px;top:909px;width:124px;height:82px;background:linear-gradient(180deg,#6f93c0 0%,#8a7a6a 50%,#4a5a3a 100%)"></div>
  <div class="abs photo" role="img" aria-label="Photo of a smiling boy on a trampoline in sunlit garden" style="left:442px;top:909px;width:124px;height:82px;background:linear-gradient(160deg,#c9c77a 0%,#6f8c3c 50%,#3f5a2a 100%)"></div>
  <div class="abs photo" role="img" aria-label="Photo of children playing on a trampoline on a bright day" style="left:574px;top:909px;width:124px;height:82px;background:linear-gradient(180deg,#b9d7ee 0%,#d8c7b0 50%,#3e3a3a 100%)"></div>
</section>

<div class="abs hline" style="top:1017px"></div>

<section>
  <h2 class="abs" style="left:92px;top:1042px">Our partners</h2>
  <div class="abs partner-mark" style="left:104px;top:1082px"></div>
  <div class="abs partner-name" style="left:130px;top:1079px">Company name<br><span>Velit esse molestie</span></div>
  <div class="abs partner-mark" style="left:222px;top:1082px"></div>
  <div class="abs partner-name" style="left:252px;top:1079px">Company name<br><span>Velit esse molestie</span></div>
  <div class="abs partner-mark" style="left:339px;top:1082px"></div>
  <div class="abs partner-name" style="left:368px;top:1079px">Company name<br><span>Velit esse molestie</span></div>
  <div class="abs partner-mark" style="left:455px;top:1082px"></div>
  <div class="abs partner-name" style="left:480px;top:1079px">Company name<br><span>Velit esse molestie</span></div>
  <div class="abs partner-mark" style="left:572px;top:1082px"></div>
  <div class="abs partner-name" style="left:602px;top:1079px">Company name<br><span>Velit esse molestie</span></div>
</section>

<footer>
  <div class="abs footer"></div>
  <div class="footer-nav">
    <a href="#" style="left:92px">Home</a>
    <a href="#" style="left:125px">Careers</a>
    <a href="#" style="left:163px">About Us</a>
    <a href="#" style="left:207px">Locations &amp; Hours</a>
    <a href="#" style="left:282px">Jumping</a>
    <a href="#" style="left:322px">Groups &amp; Events</a>
    <a href="#" style="left:391px">Gallery</a>
    <a href="#" style="left:427px">Safety</a>
    <a href="#" style="left:461px">Latest News</a>
  </div>
  <div class="abs copy">2014 © Privacy Policy</div>
  <div class="abs" style="left:610px;top:1142px">
    <div class="logo" style="color:#888;font-size:19px">HOPZONE</div>
    <div class="logo-sub" style="font-size:6px">Trampolines</div>
  </div>
</footer>

</body>
</html>
```